IT Consulting Site Revamping for Marlune

I've put a skeleton together on my website, but realize I need some help (it's http://pilot.marlune-example.ca).
I've pulled together tidbits from other websites, but really need my site to be cleaned up, and really spruced up.
I primarily focus on the IT needs of small to medium size businesses, taking care of everything from their servers and networks down to their workstations.
I also want a page listing the vendors (and logos) that I work with including Quillsoft, Zentrix, Halvor, Brax, TL, RZO, VELK, Trevo, Gatemoor.
There should also be a simple form to get a quote that will email me.
The final design should communicate strength and reliability.
I would like this to be a fully functional website, that I can upload to Plumly Pages, with the same sort of pages that are existing on http://pilot.marlune-example.ca
Updates
Hey everyone,
Hi everyone,
Reason: Hi all,
There are some designers that would like to submit some new designs, so I'm extending the deadline.
Thanks,
Target Market(s)
Small to medium size business owners. This will primarily be males who work in the oil and gas industry.
Industry/Entity Type
Consulting
Look and feel
Each slider illustrates characteristics of the customer's brand and the style your logo design should communicate.

```html
<!DOCTYPE html>
<html lang="en">
<head>
<meta charset="utf-8">
<title>Marlune Solutions – IT Support for Small Business</title>
<link href="https://fonts.googleapis.com/css2?family=Arimo:wght@400;700&family=Noto+Sans:wght@400;700&family=Roboto+Condensed:wght@400&display=swap" rel="stylesheet">
<style>
:root{
  --brand:#2b7cc1;
  --heading:#2f6aa3;
  --orange:#f7941d;
  --orange-dark:#e9821a;
  --band:#93b9d9;
  --panel:#d5e5f1;
  --rule:#86b3d8;
  --text:#333;
  --header-bg:#f2f2f2;
}
*{box-sizing:border-box;margin:0;padding:0}
html,body{width:976px;height:1200px;overflow:hidden;background:#fff}
body{position:relative;font-family:"Noto Sans",sans-serif;color:var(--text)}
.abs{position:absolute}

/* header */
.site-header{left:0;top:0;width:976px;height:95px;background:var(--header-bg)}
.brand{left:127px;top:12px;display:flex;align-items:center;gap:12px}
.brand-dot{width:62px;height:62px;border-radius:50%;background:var(--brand)}
.brand-name{font-family:"Arimo",sans-serif;font-weight:700;font-size:40px;color:var(--brand);line-height:1}
.brand-sub{font-family:"Arimo",sans-serif;font-size:12px;letter-spacing:9px;color:#555;margin-top:2px}
.phone{left:711px;top:16px;display:flex;align-items:center;gap:8px;font-family:"Arimo",sans-serif;font-size:19px;color:var(--brand)}
.quote-btn{left:693px;top:50px;width:172px;height:29px;background:var(--orange);color:#fff;font-family:"Arimo",sans-serif;font-size:13px;white-space:nowrap;display:flex;align-items:center;justify-content:center;border-radius:2px}

.main-nav{left:0;top:95px;width:976px;height:27px;background:linear-gradient(#e6e6e6,#c9c9c9);border-top:1px solid #bbb}
.main-nav ul{list-style:none;position:absolute;left:0;top:0;width:100%;height:27px;font-family:"Arimo",sans-serif;font-size:13px;color:var(--brand)}
.main-nav li{position:absolute;top:6px;white-space:nowrap}
.caret{display:inline-block;width:0;height:0;border-left:4px solid transparent;border-right:4px solid transparent;border-top:6px solid var(--brand);margin-left:5px;vertical-align:2px}
.nav-pointer{left:150px;top:116px;width:0;height:0;border-left:6px solid transparent;border-right:6px solid transparent;border-bottom:6px solid #fff}

/* hero */
.hero-art{left:444px;top:133px;width:468px;height:336px;background:radial-gradient(ellipse at 55% 50%,#dfe5ec 0%,#eef2f6 45%,#fff 75%)}
.hero-title{left:110px;top:155px;z-index:2;white-space:nowrap;font-family:"Arimo",sans-serif;font-size:35px;line-height:43px;color:#333;font-weight:400}
.hero-copy{left:110px;top:248px;z-index:2;white-space:nowrap;font-family:"Arimo",sans-serif;font-size:13.3px;line-height:15.5px;color:#333}
.btn{background:var(--orange);color:#fff;font-family:"Noto Sans",sans-serif;font-size:11px;white-space:nowrap;display:flex;align-items:center;padding-left:8px;text-transform:uppercase;border:1px solid var(--orange-dark)}
.btn .chev{margin-left:auto;margin-right:6px;font-size:15px;font-weight:700}
.hero-btn{left:111px;top:332px;width:200px;height:24px;z-index:2}

/* help band */
.help-band{left:64px;top:479px;width:847px;height:57px;background:var(--band);display:flex;align-items:center;justify-content:center;font-family:"Roboto Condensed",sans-serif;font-size:29px;color:#fff}
.help-notch{left:478px;top:479px;width:0;height:0;border-left:9px solid transparent;border-right:9px solid transparent;border-top:10px solid #fff}

.service{top:564px;width:190px}
.service h3{font-size:14px;font-weight:400;color:var(--heading);text-transform:uppercase;margin-bottom:11px;letter-spacing:.2px;white-space:nowrap}
.service li{list-style:none;font-size:11.3px;line-height:17.7px;color:#333;white-space:nowrap}
.service .btn{position:absolute;top:114px;width:94px;height:24px}

/* partners panel */
.partners{left:64px;top:737px;width:846px;height:214px;background:var(--panel)}
.panel-h{font-size:14px;font-weight:400;color:var(--heading);text-transform:uppercase;white-space:nowrap}
.panel-p{font-size:11.2px;line-height:16.9px;color:#444;white-space:nowrap}
.vendors{left:352px;top:768px;width:270px;display:grid;grid-template-columns:repeat(3,1fr);row-gap:16px;column-gap:6px;font-weight:700;font-size:16px;color:#1e4f86;text-align:center}

/* footer */
.footer-rule{top:963px;width:1px;height:163px;background:var(--rule)}
.foot-h{font-size:14px;font-weight:400;color:var(--heading);text-transform:uppercase;white-space:nowrap}
.foot-links li{list-style:none;font-size:10px;line-height:14.4px;color:#333}
.social{left:220px;width:104px;height:28px;border-radius:2px;color:#fff;font-family:"Arimo",sans-serif;font-size:11px;font-weight:700;display:flex;align-items:center}
.social .sq{width:34px;height:100%;display:flex;align-items:center;justify-content:center;border-right:1px solid rgba(255,255,255,.35)}
.social .sq span{width:12px;height:12px;background:#fff;opacity:.85}
.social .lbl{flex:1;text-align:center}
.s-a{background:#5a7fbf}.s-b{background:#4db3c7}.s-c{background:#5b5b5b}
.contact-big{font-size:13.5px;color:#333;white-space:nowrap}
.contact-small{font-size:10px;color:#333;white-space:nowrap}
.email-field{left:654px;top:1007px;width:174px;height:21px;border:1px solid #8fb2d2;background:#fff;font-size:10px;color:#888;padding-left:6px;line-height:19px}
.email-go{left:808px;top:1007px;width:20px;height:21px;background:var(--brand);color:#fff;font-weight:700;font-size:13px;text-align:center;line-height:20px}
.news-copy{left:654px;top:1034px;font-size:10px;line-height:14.5px;color:#333;white-space:nowrap}
.legal-rule{left:210px;top:1145px;width:530px;height:2px;background:radial-gradient(ellipse,#ddd,transparent 70%)}
.legal{left:0;top:1159px;width:976px;text-align:center;font-family:"Arimo",sans-serif;font-size:9px;color:#333}
.legal b{margin-right:10px}
</style>
</head>
<body>

<header class="abs site-header"></header>
<div class="abs brand">
  <div class="brand-dot"></div>
  <div>
    <div class="brand-name">marlune</div>
    <div class="brand-sub">solutions</div>
  </div>
</div>
<div class="abs phone">
  <svg width="26" height="26" viewBox="0 0 26 26"><circle cx="13" cy="13" r="11.5" fill="none" stroke="#2b7cc1" stroke-width="2"/><path d="M9 7.5c-1 1-1.2 2.6-.3 4.4 1.2 2.4 3 4.3 5.4 5.6 1.7.9 3.3.7 4.4-.3l-2.2-2.2-1.6 1c-1.6-.8-2.9-2.1-3.6-3.6l1-1.6z" fill="#2b7cc1"/></svg>
  <span>555 010 4421</span>
</div>
<div class="abs quote-btn">GET FREE QUOTE ONLINE</div>

<nav class="abs main-nav">
  <ul>
    <li style="left:142px">Home</li>
    <li style="left:235px">About Us</li>
    <li style="left:337px">Services<span class="caret"></span></li>
    <li style="left:436px">Products<span class="caret"></span></li>
    <li style="left:544px">Contact</li>
  </ul>
</nav>
<div class="abs nav-pointer"></div>

<div class="abs hero-art" role="img" aria-label="Illustration of a central server rack linked by arrows to surrounding desktop workstations"></div>
<h1 class="abs hero-title">Hidden Network Problems<br>Cost Money</h1>
<p class="abs hero-copy">We can detect hidden network problems<br>and provide ongoing technical support<br>for your small business.</p>
<div class="abs btn hero-btn">Get a free network assesment<span class="chev">›</span></div>

<div class="abs help-band">How can we help your business?</div>
<div class="abs help-notch"></div>

<section class="abs service" style="left:114px">
  <h3>Managed IT Services</h3>
  <ul><li>Reduced Downtime</li><li>Improved Productivity</li><li>Innovative Applications</li><li>Critical Data Protection</li></ul>
  <div class="btn" style="left:0">Learn more<span class="chev">›</span></div>
</section>
<section class="abs service" style="left:303px">
  <h3>Networking</h3>
  <ul><li>Computer Networking</li><li>Firewalls</li><li>Virtual Private Networks (VPN)</li><li>Remote Access</li></ul>
  <div class="btn" style="left:0">Learn more<span class="chev">›</span></div>
</section>
<section class="abs service" style="left:502px">
  <h3>Back Up &amp; Recovery</h3>
  <ul><li>Data Back Up</li><li>Data Recovery</li><li>Storage and Virtualization</li></ul>
  <div class="btn" style="left:0">Learn more<span class="chev">›</span></div>
</section>
<section class="abs service" style="left:701px">
  <h3>Computer Repair</h3>
  <ul><li>Spyware Removal</li><li>Virus Removal</li><li>On Site Repair Service</li></ul>
  <div class="btn" style="left:0">Learn more<span class="chev">›</span></div>
</section>

<div class="abs partners"></div>
<h3 class="abs panel-h" style="left:111px;top:766px">Small Business Specialists</h3>
<p class="abs panel-p" style="left:111px;top:790px">We've been trusted for over the last<br>7 years by small business in Calgary for<br>being flexible, easy going, and affordable.<br>We have partnered with the industry giants<br>to provide smart and affordable IT solutions.</p>
<div class="abs btn" style="left:111px;top:897px;width:199px;height:24px">See what we can do for you<span class="chev">›</span></div>

<div class="abs vendors">
  <span>Quillsoft</span><span>Halvor</span><span>TL</span>
  <span>Zentrix</span><span>Brax</span><span>VELK</span>
  <span>RZO</span><span>Trevo</span><span>Gatemoor</span>
</div>

<h3 class="abs panel-h" style="left:645px;top:766px">Calgary's IT Experts</h3>
<p class="abs panel-p" style="left:645px;top:790px">We have been recognised by many business<br>owners for our dedication to delivering excep-<br>tional business computer support services and<br>IT solutions. Our trained and experienced IT<br>professionals deliver all day, and every day,<br>rapid issue resolution, ongoing support, main-<br>tenance and stability that your business<br>deserves and can depend upon.</p>

<h3 class="abs foot-h" style="left:128px;top:981px">About Us</h3>
<ul class="abs foot-links" style="left:127px;top:1009px">
  <li>About Us</li><li>Testimonials</li><li>Technical Blog</li><li>Newsletter</li><li>Contact Us</li>
</ul>
<div class="abs social s-a" style="top:984px"><div class="sq"><span></span></div><div class="lbl">Friendloop</div></div>
<div class="abs social s-b" style="top:1019px"><div class="sq"><span></span></div><div class="lbl">Chirpline</div></div>
<div class="abs social s-c" style="top:1055px"><div class="sq"><span></span></div><div class="lbl">Linkwell</div></div>

<div class="abs footer-rule" style="left:358px"></div>
<h3 class="abs foot-h" style="left:381px;top:981px">Contact Us</h3>
<div class="abs contact-big" style="left:382px;top:1005px">Call 555 010 7730</div>
<div class="abs contact-small" style="left:382px;top:1024px">24/7 Tech Support</div>
<div class="abs contact-big" style="left:382px;top:1049px">Office Location</div>
<div class="abs contact-small" style="left:382px;top:1068px">PO Box 4410, Calgary, AB, T2T 0A1</div>

<div class="abs footer-rule" style="left:623px"></div>
<h3 class="abs foot-h" style="left:654px;top:981px">Sign Up For Newsletter</h3>
<div class="abs email-field">Your email address...</div>
<div class="abs email-go">›</div>
<p class="abs news-copy">Read our monthly email newslette to stay<br>updated on technology that can help you<br>grow your business better.</p>

<div class="abs legal-rule"></div>
<div class="abs legal">© 2012 <b>Marlune Solutions</b> <b style="margin:0">HOME | ABOUT US | SERVICES | PRODUCTS | CONTACT</b></div>

</body>
</html>
```